Business Card Design for Boutique Agriculture Consulting Practice

Develop a modern Business card design using uploaded logos . Using the color specs 6C344F rgb(108, 52, 79) The fonts are trajan pro and eurostile. The business owner is a woman and should have a hint of femininity. This is what is behind the naming of the company: Rock roads are synonymous with the rural US landscape, where the corn grows and the cattle graze or for Fern Gully Advisory home. But don’t let the dust get in your eyes, rock roads have edge and are often the only path to a spectacular destination. To navigate them one must know where they are going, have the courage to take a new path and the willingness to adjust their plans to get there.
Target Market(s)
Marketing Professionals
Industry/Entity Type
Agriculture
Contact Information for Business Card
Maribeth Tolland
Title: Founder and CEO
Address: 20473 Wesley Lane, Carver Plains 66218
Email: mt@ferngullyadvisory.com
Phone: 555.554.2019
Website: www.ferngullyadvisory.com
Font styles to use
Other font styles liked:
- trajan pro and eurostile
Requirements
Must have
- Please use the correct color specs. Logo color specs are 6C344F rgb(108, 52, 79) The fonts are trajan pro and eurostile. Name, email and phone be the most important information included on the card
Should not have
- additional graphics

```html
<!DOCTYPE html>
<html lang="en">
<head>
<meta charset="utf-8">
<title>Fern Gully Advisory – Business Card</title>
<link rel="stylesheet" href="https://fonts.googleapis.com/css2?family=Cinzel:wght@400;700&family=Michroma&display=swap">
<style>
  :root {
    --plum: #6c344f;
    --plum-soft: #b0748f;
    --paper: #ffffff;
    --ink-faint: #f1eef0;
    --front-text: #f5eef2;
    --backdrop: #d9d6d8;
  }
  html, body {
    margin: 0;
    padding: 0;
    width: 801px;
    height: 1200px;
    overflow: hidden;
    background: var(--backdrop);
  }
  .canvas {
    position: relative;
    width: 801px;
    height: 1200px;
  }
  .card {
    position: absolute;
    left: 80px;
    width: 640px;
    height: 366px;
    box-shadow: 0 10px 30px rgba(0,0,0,0.25);
    overflow: hidden;
  }
  .card--front {
    top: 150px;
    background: var(--plum);
  }
  .card--back {
    top: 690px;
    background: var(--paper);
  }

  /* front */
  .front-brand {
    position: absolute;
    left: 0; right: 0;
    top: 122px;
    text-align: center;
    font-family: "Cinzel", serif;
    font-weight: 700;
    font-size: 40px;
    letter-spacing: 1px;
    color: var(--plum-soft);
  }
  .front-web {
    position: absolute;
    left: 0; right: 0;
    top: 230px;
    text-align: center;
    font-family: "Cinzel", serif;
    font-size: 19px;
    letter-spacing: 0.5px;
    color: var(--front-text);
  }

  /* back */
  .back-watermark {
    position: absolute;
    inset: 0;
    background: radial-gradient(ellipse at 45% 50%, var(--ink-faint), rgba(255,255,255,0) 70%);
  }
  .contact {
    position: absolute;
    left: 38px;
    top: 120px;
    color: var(--plum);
  }
  .contact__name {
    font-family: "Cinzel", serif;
    font-weight: 700;
    font-size: 24px;
    margin: 0;
  }
  .contact__title {
    font-family: "Michroma", sans-serif;
    font-size: 11px;
    margin: 4px 0 0;
    padding-bottom: 8px;
    border-bottom: 1px solid var(--plum);
    width: 270px;
  }
  .contact__list {
    list-style: none;
    margin: 10px 0 0;
    padding: 0;
    font-family: "Michroma", sans-serif;
    font-size: 11.5px;
    line-height: 24px;
  }
  .contact__list li {
    display: flex;
    align-items: center;
    gap: 8px;
  }
  .contact__list svg { flex: none; }
  .brand {
    position: absolute;
    right: 40px;
    top: 118px;
    width: 220px;
    text-align: center;
    font-family: "Cinzel", serif;
    font-weight: 700;
    font-size: 24px;
    line-height: 1.15;
    color: var(--plum);
  }
</style>
</head>
<body>
<div class="canvas">
  <section class="card card--front">
    <div class="front-brand">Fern Gully Advisory</div>
    <div class="front-web">www.FernGullyAdvisory.com</div>
  </section>

  <section class="card card--back">
    <div class="back-watermark" role="img" aria-label="Faint repeated script company name pattern"></div>
    <div class="contact">
      <h1 class="contact__name">Maribeth Tolland</h1>
      <p class="contact__title">FOUNDER AND CEO</p>
      <ul class="contact__list">
        <li>
          <svg width="14" height="14" viewBox="0 0 14 14" aria-hidden="true"><circle cx="7" cy="7" r="7" fill="var(--plum)"/><path d="M4.5 4 L6 4 L6.5 5.5 L5.7 6.2 Q6.5 7.8 7.8 8.3 L8.5 7.5 L10 8 L10 9.5 Q6 10 4.5 5.5 Z" fill="#fff"/></svg>
          555.554.2019
        </li>
        <li>
          <svg width="14" height="14" viewBox="0 0 14 14" aria-hidden="true"><circle cx="7" cy="7" r="7" fill="var(--plum)"/><rect x="3.5" y="4.5" width="7" height="5" fill="#fff"/><path d="M3.5 4.5 L7 7.3 L10.5 4.5" stroke="var(--plum)" stroke-width="0.8" fill="none"/></svg>
          mt@ferngullyadvisory.com
        </li>
        <li>20473 Wesley Lane, Carver Plains 66218</li>
      </ul>
    </div>
    <div class="brand">Fern Gully Advisory</div>
  </section>
</div>
</body>
</html>
```